Brenvick Holdings LLC, new Business cards

I'm moving offices and need new cards. Plus I'm open to modifying the current design of my card. I will keep the logo but would like to explore other layouts and fonts for the design. I've included the current double sided card for reference. I Like the navy color and white. Might be open to grays or silver. Needs to be clean and elegant.

Target Market(s)

Investors, buyers & sellers of private equities and real estate.

Contact Information for Business Card

Brenvick Holdings
Dorian P.K. Halvers, Managing Principal
418 Ostrander Ave., Suite 612
Denver, CO 80319
M: 970-555-0147, O: 303-555-0192
Dorian@brenvickholdings.example
Brenvickholdings.example

Colors
0354a2
ffffff
c4c4c4

Requirements
Must have
• Business card details.
• Logo raised or embossed, it was designed after a wax seal. Current has raised ink.
Nice to have
• Space on card to write additional notes.

```html
<!DOCTYPE html>
<html lang="en">
<head>
<meta charset="utf-8">
<title>Brenvick Holdings — Business Card</title>
<link rel="stylesheet" href="https://fonts.googleapis.com/css2?family=Libre+Baskerville:wght@400;700&family=Montserrat:wght@600;700&display=swap">
<style>
  :root {
    --backdrop: #37345f;
    --navy: #2b2960;
    --navy-deep: #262458;
    --slate: #56537f;
    --slate-dark: #3e3b6c;
    --white: #ffffff;
    --blue-light: #4aa2e6;
    --blue-mid: #3f74d6;
    --blue-deep: #2a5bbf;
  }
  html, body {
    margin: 0;
    padding: 0;
    width: 1038px;
    height: 1200px;
    overflow: hidden;
    background: var(--backdrop);
  }
  .card {
    position: absolute;
    left: 48px;
    width: 932px;
    height: 532px;
    background: var(--white);
    overflow: hidden;
  }
  .card--front { top: 44px; }
  .card--back { top: 624px; height: 536px; }
  .card__art {
    position: absolute;
    inset: 0;
    width: 100%;
    height: 100%;
  }
  .brand {
    position: absolute;
    left: 0;
    right: 0;
    top: 176px;
    display: flex;
    flex-direction: column;
    align-items: center;
    gap: 26px;
  }
  .brand__mark {
    width: 84px;
    height: 84px;
    border-radius: 50%;
    background: var(--navy);
  }
  .brand__name {
    font-family: "Libre Baskerville", serif;
    font-weight: 400;
    font-size: 36px;
    letter-spacing: 3px;
    color: var(--navy);
    text-transform: uppercase;
    white-space: nowrap;
  }
  .person {
    position: absolute;
    right: 140px;
    top: 50px;
    text-align: right;
    color: var(--navy);
    font-family: "Libre Baskerville", serif;
  }
  .person__name {
    margin: 0;
    font-size: 33px;
    font-weight: 400;
    line-height: 1.1;
    text-transform: uppercase;
    white-space: nowrap;
  }
  .person__role {
    margin: 10px 0 0;
    font-size: 17px;
    font-weight: 700;
    text-transform: uppercase;
  }
  .contacts {
    position: absolute;
    left: 66px;
    top: 180px;
    margin: 0;
    padding: 0;
    list-style: none;
  }
  .contact {
    display: flex;
    align-items: center;
    height: 60px;
    margin-bottom: 24px;
    font-family: "Montserrat", sans-serif;
    font-weight: 700;
    font-size: 17px;
    line-height: 1.45;
    color: var(--navy);
    text-transform: uppercase;
    white-space: nowrap;
  }
  .contact__icon {
    width: 60px;
    height: 60px;
    margin-right: 46px;
    flex: none;
  }
</style>
</head>
<body>

<section class="card card--front">
  <svg class="card__art" viewBox="0 0 932 532" aria-hidden="true">
    <polygon points="0,0 470,0 0,470" fill="var(--navy-deep)"/>
    <polygon points="0,0 330,0 0,330" fill="var(--slate)"/>
    <polygon points="0,0 200,0 0,200" fill="var(--navy-deep)"/>
    <polygon points="0,0 100,0 0,100" fill="var(--slate-dark)"/>
    <polygon points="932,170 932,532 600,532" fill="var(--slate)"/>
    <polygon points="932,300 932,532 740,532" fill="var(--navy-deep)"/>
  </svg>
  <div class="brand">
    <span class="brand__mark"></span>
    <span class="brand__name">Brenvick Holdings</span>
  </div>
</section>

<section class="card card--back">
  <svg class="card__art" viewBox="0 0 932 536" aria-hidden="true">
    <defs>
      <linearGradient id="blue-sweep" x1="0" y1="1" x2="1" y2="0">
        <stop offset="0" stop-color="var(--blue-mid)"/>
        <stop offset="1" stop-color="var(--blue-light)"/>
      </linearGradient>
    </defs>
    <polygon points="520,424 890,70 932,70 932,424" fill="url(#blue-sweep)"/>
    <polygon points="640,424 760,230 932,230 932,424" fill="var(--blue-deep)"/>
    <polygon points="660,536 932,280 932,536" fill="var(--navy-deep)"/>
  </svg>

  <div class="person">
    <h1 class="person__name">Dorian P.K. Halvers</h1>
    <p class="person__role">Managing Principal</p>
  </div>

  <ul class="contacts">
    <li class="contact">
      <svg class="contact__icon" viewBox="0 0 60 60" aria-hidden="true">
        <circle cx="30" cy="30" r="30" fill="var(--navy)"/>
        <path d="M30 15c-6 0-10.5 4.5-10.5 10.3 0 7.7 10.5 19.7 10.5 19.7s10.5-12 10.5-19.7C40.5 19.5 36 15 30 15z" fill="var(--white)"/>
        <circle cx="30" cy="25.5" r="4" fill="var(--navy)"/>
      </svg>
      <span>418 Ostrander Ave., Suite 612<br>Denver, CO 80319</span>
    </li>
    <li class="contact">
      <svg class="contact__icon" viewBox="0 0 60 60" aria-hidden="true">
        <circle cx="30" cy="30" r="30" fill="var(--navy)"/>
        <g fill="none" stroke="var(--white)" stroke-width="2.4">
          <rect x="17" y="20" width="26" height="19" rx="1.5"/>
          <polyline points="17,21 30,31 43,21"/>
          <line x1="17" y1="39" x2="26" y2="29"/>
          <line x1="34" y1="29" x2="43" y2="39"/>
        </g>
      </svg>
      <span>Dorian@brenvickholdings.example</span>
    </li>
    <li class="contact">
      <svg class="contact__icon" viewBox="0 0 60 60" aria-hidden="true">
        <circle cx="30" cy="30" r="30" fill="var(--navy)"/>
        <path d="M21 16l5.5-1 3.5 8-3.5 2.5c1.5 4 4.5 7 8.5 8.5l2.5-3.5 8 3.5-1 5.5c-12 1.5-25-11.5-23.5-23.5z" fill="var(--white)"/>
      </svg>
      <span>M: 970-555-0147 &middot; O: 303-555-0192</span>
    </li>
    <li class="contact">
      <svg class="contact__icon" viewBox="0 0 60 60" aria-hidden="true">
        <circle cx="30" cy="30" r="30" fill="var(--navy)"/>
        <g fill="none" stroke="var(--white)" stroke-width="2.2">
          <circle cx="30" cy="30" r="13"/>
          <ellipse cx="30" cy="30" rx="5.5" ry="13"/>
          <line x1="17" y1="30" x2="43" y2="30"/>
          <line x1="19" y1="23.5" x2="41" y2="23.5"/>
          <line x1="19" y1="36.5" x2="41" y2="36.5"/>
        </g>
      </svg>
      <span>Brenvickholdings.example</span>
    </li>
  </ul>
</section>

</body>
</html>
```